Private Investment Firm Needs PowerPoint Presentation Template

Design PowerPoint template, take Ridgeholm-submitted rough presentation draft, and drop it into new template. See attached Project Brief file for more detail.
Updates

Some decent designs have been submitted but they seem to lack the understanding of our target markets. I am hopeful that more time and feedback will result in better results.

Target Market(s)

Private company owners and intermediaries.

Font styles to use
Serif

Colors
3176b5

Requirements
Must have
• See attached Project Brief.
Nice to have
Should not have
• No B2C fluff--this is a B2B project.

```html
<!DOCTYPE html>
<html lang="en">
<head>
<meta charset="utf-8">
<title>Non-Control Investor Questionnaire – Slide Options</title>
<link rel="stylesheet" href="https://fonts.googleapis.com/css2?family=Arimo:wght@400;700&family=Carlito:wght@400;700&display=swap">
<style>
  :root {
    --brand: #3176b5;
    --brand-deep: #1a64b4;
    --ink: #111;
    --grey: #7a7a7a;
    --link: #2d6fb0;
    --canvas: #e6e6f4;
    --panel: #dfe7f1;
    --white: #fff;
  }
  * { box-sizing: border-box; margin: 0; padding: 0; }
  html, body { width: 1200px; height: 682px; overflow: hidden; }
  body { background: var(--canvas); font-family: "Arimo", Arial, sans-serif; position: relative; }

  .slide {
    position: absolute; width: 594px; height: 333px;
    background: var(--white); overflow: hidden;
  }
  .slide--tl { left: 4px; top: 4px; }
  .slide--tr { left: 602px; top: 4px; }
  .slide--bl { left: 4px; top: 344px; }
  .slide--br { left: 602px; top: 344px; }

  .side-panel {
    position: absolute; right: 0; top: 0; width: 112px; height: 100%;
    background: linear-gradient(180deg, var(--panel), #eef2f8 70%, var(--panel));
  }
  .title-bar {
    position: absolute; left: 13px; top: 1px; width: 12px; height: 52px;
    background: var(--brand-deep);
  }
  .title {
    position: absolute; left: 33px; top: 9px; width: 450px;
    font-weight: 700; font-size: 19.5px; line-height: 21px;
    color: var(--brand-deep);
  }
  .subtitle {
    position: absolute; left: 34px; top: 51px; width: 440px;
    font-size: 9.3px; line-height: 13px; color: var(--grey);
  }
  .tag {
    position: absolute; right: 114px; top: 64px;
    font-size: 8.4px; font-weight: 700; color: var(--grey);
  }

  .questions { position: absolute; left: 13px; top: 81px; width: 463px; list-style: none; }
  .q {
    position: relative; padding-left: 25px; margin-bottom: 1.5px;
    font-family: "Carlito", Calibri, sans-serif;
    font-size: 8px; line-height: 10.5px; color: var(--ink);
  }
  .q strong { font-weight: 700; }
  .q .best { color: var(--link); text-decoration: underline; }
  .q .u { text-decoration: underline; }
  .q svg { position: absolute; left: 0; top: -3px; width: 17px; height: 17px; }
  .q--wide { padding-left: 23px; }

  .bullet { fill: var(--brand); }
  .bullet-ring { fill: none; stroke: var(--brand); stroke-width: 3; }

  .brand {
    position: absolute; left: 10px; top: 308px;
    display: flex; align-items: center; gap: 5px;
  }
  .brand-square { width: 10px; height: 10px; background: var(--brand-deep); }
  .brand-name {
    font-family: "Arimo", Arial, sans-serif; font-size: 14px; font-weight: 700;
    color: var(--brand-deep); line-height: 16px;
  }
  .foot-bar { position: absolute; left: 114px; top: 314px; width: 431px; height: 10px; background: var(--brand-deep); }
  .foot-square { position: absolute; left: 567px; top: 308px; width: 27px; height: 22px; background: var(--brand-deep); }
</style>
</head>
<body>

<!-- Option A: hexagon bullets -->
<section class="slide slide--tl">
  <div class="side-panel"></div>
  <div class="title-bar"></div>
  <h1 class="title">THE CRITICAL QUESTIONS TO ASK OF ANY PROSPECTIVE NON-CONTROL INVESTOR</h1>
  <p class="subtitle">Non-Control Capital is a specialty, so only those firms with deep experience investing it as a team should be considered</p>
  <p class="tag">Non-Control Capital Questionnaire</p>
  <ul class="questions">
    <li class="q"><svg viewBox="0 0 20 20"><polygon class="bullet" points="10,1 18,5.5 18,14.5 10,19 2,14.5 2,5.5"/></svg><strong>Question #1: How many years has the firm been investing Non-Control Capital?</strong><br><span class="best">Best Answer</span>: 5+ years investing as a team within the current firm<br>Indicates comfort and experience evaluating and making NCC investments with each other and increases likelihood of close</li>
    <li class="q"><svg viewBox="0 0 20 20"><polygon class="bullet" points="10,1 18,5.5 18,14.5 10,19 2,14.5 2,5.5"/></svg><strong>Question #2: How may fully-invested Non-Control Capital funds in the firm’s history?</strong><br><span class="best">Best Answer</span>: 2+ fully-invested funds - Indicates experience and ability to close deals with the current regime—those firms without it may only be testing the waters and not have a long-term commitment to NCC investing</li>
    <li class="q"><svg viewBox="0 0 20 20"><polygon class="bullet" points="10,1 18,5.5 18,14.5 10,19 2,14.5 2,5.5"/></svg><strong>Question #3: What percentage of the firm’s voting investment committee are full-time Non-Control Capital investors?</strong><br><span class="best">Best Answer</span>: Super-majority - Indicates commitment, experience, and focus on NCC and overcomes dependency on buyout heritage, if any</li>
    <li class="q"><svg viewBox="0 0 20 20"><polygon class="bullet" points="10,1 18,5.5 18,14.5 10,19 2,14.5 2,5.5"/></svg><strong>Question #4: What is the number of Non-Control Capital investments made with the <span class="u">current firm and team</span>?</strong><br><span class="best">Best Answer</span>: 20+ - Indicates long-term experience and comfort with current team, investment committee, and NCC investment assessment</li>
    <li class="q"><svg viewBox="0 0 20 20"><polygon class="bullet" points="10,1 18,5.5 18,14.5 10,19 2,14.5 2,5.5"/></svg><strong>Question #5: What percentage of portfolio investments made are “sponsorless” (those without a change-of-control investor)?</strong><span class="best">Best Answer</span>: 80%+ of all investments closed in the last 5 years (assumes current transaction is also sponsorless) Indicates ability to add-value as a sole minority investor and not simply as a back-up to another sponsor</li>
    <li class="q q--wide"><svg viewBox="0 0 20 20"><polygon class="bullet" points="10,1 18,5.5 18,14.5 10,19 2,14.5 2,5.5"/></svg><strong>Question #6: Can the investor show quantifiable proof of their ability to assist portfolio companies with growth and improvement (assumes more than 20 exited Non-Control investments)?:</strong><br><span class="best">Best Answer</span>: Yes (company owners should evaluate investors on actual historical revenue, EBITDA, and employee growth impact and the results should exceed what the current management has achieved on their own over the past 3 years) - Indicates true value-added ability to help owners grow their businesses. Those without proof of their impact, or who are unwilling to disclose it, should be excluded</li>
  </ul>
  <div class="brand"><span class="brand-square"></span><span class="brand-name">Ridgeholm</span></div>
  <div class="foot-bar"></div>
  <div class="foot-square"></div>
</section>

<!-- Option B: large hexagon bullets -->
<section class="slide slide--tr">
  <div class="side-panel"></div>
  <div class="title-bar"></div>
  <h1 class="title">THE CRITICAL QUESTIONS TO ASK OF ANY PROSPECTIVE NON-CONTROL INVESTOR</h1>
  <p class="subtitle">Non-Control Capital is a specialty, so only those firms with deep experience investing it as a team should be considered</p>
  <p class="tag">Non-Control Capital Questionnaire</p>
  <ul class="questions">
    <li class="q"><svg viewBox="0 0 20 20"><polygon class="bullet" points="10,0 19.5,5 19.5,15 10,20 0.5,15 0.5,5"/></svg><strong>Question #1: How many years has the firm been investing Non-Control Capital?</strong><br><span class="best">Best Answer</span>: 5+ years investing as a team within the current firm<br>Indicates comfort and experience evaluating and making NCC investments with each other and increases likelihood of close</li>
    <li class="q"><svg viewBox="0 0 20 20"><polygon class="bullet" points="10,0 19.5,5 19.5,15 10,20 0.5,15 0.5,5"/></svg><strong>Question #2: How may fully-invested Non-Control Capital funds in the firm’s history?</strong><br><span class="best">Best Answer</span>: 2+ fully-invested funds - Indicates experience and ability to close deals with the current regime—those firms without it may only be testing the waters and not have a long-term commitment to NCC investing</li>
    <li class="q"><svg viewBox="0 0 20 20"><polygon class="bullet" points="10,0 19.5,5 19.5,15 10,20 0.5,15 0.5,5"/></svg><strong>Question #3: What percentage of the firm’s voting investment committee are full-time Non-Control Capital investors?</strong><br><span class="best">Best Answer</span>: Super-majority - Indicates commitment, experience, and focus on NCC and overcomes dependency on buyout heritage, if any</li>
    <li class="q"><svg viewBox="0 0 20 20"><polygon class="bullet" points="10,0 19.5,5 19.5,15 10,20 0.5,15 0.5,5"/></svg><strong>Question #4: What is the number of Non-Control Capital investments made with the <span class="u">current firm and team</span>?</strong><br><span class="best">Best Answer</span>: 20+ - Indicates long-term experience and comfort with current team, investment committee, and NCC investment assessment</li>
    <li class="q"><svg viewBox="0 0 20 20"><polygon class="bullet" points="10,0 19.5,5 19.5,15 10,20 0.5,15 0.5,5"/></svg><strong>Question #5: What percentage of portfolio investments made are “sponsorless” (those without a change-of-control investor)?</strong><span class="best">Best Answer</span>: 80%+ of all investments closed in the last 5 years (assumes current transaction is also sponsorless) Indicates ability to add-value as a sole minority investor and not simply as a back-up to another sponsor</li>
    <li class="q q--wide"><svg viewBox="0 0 20 20"><polygon class="bullet" points="10,0 19.5,5 19.5,15 10,20 0.5,15 0.5,5"/></svg><strong>Question #6: Can the investor show quantifiable proof of their ability to assist portfolio companies with growth and improvement (assumes more than 20 exited Non-Control investments)?:</strong><br><span class="best">Best Answer</span>: Yes (company owners should evaluate investors on actual historical revenue, EBITDA, and employee growth impact and the results should exceed what the current management has achieved on their own over the past 3 years) - Indicates true value-added ability to help owners grow their businesses. Those without proof of their impact, or who are unwilling to disclose it, should be excluded</li>
  </ul>
  <div class="brand"><span class="brand-square"></span><span class="brand-name">Ridgeholm</span></div>
  <div class="foot-bar"></div>
  <div class="foot-square"></div>
</section>

<!-- Option C: chevron bullets -->
<section class="slide slide--bl">
  <div class="side-panel"></div>
  <div class="title-bar"></div>
  <h1 class="title">THE CRITICAL QUESTIONS TO ASK OF ANY PROSPECTIVE NON-CONTROL INVESTOR</h1>
  <p class="subtitle">Non-Control Capital is a specialty, so only those firms with deep experience investing it as a team should be considered</p>
  <p class="tag">Non-Control Capital Questionnaire</p>
  <ul class="questions">
    <li class="q"><svg viewBox="0 0 20 20"><polygon class="bullet" points="1,2 6,2 10,10 14,2 19,2 10,19"/></svg><strong>Question #1: How many years has the firm been investing Non-Control Capital?</strong><br><span class="best">Best Answer</span>: 5+ years investing as a team within the current firm<br>Indicates comfort and experience evaluating and making NCC investments with each other and increases likelihood of close</li>
    <li class="q"><svg viewBox="0 0 20 20"><polygon class="bullet" points="1,2 6,2 10,10 14,2 19,2 10,19"/></svg><strong>Question #2: How may fully-invested Non-Control Capital funds in the firm’s history?</strong><br><span class="best">Best Answer</span>: 2+ fully-invested funds - Indicates experience and ability to close deals with the current regime—those firms without it may only be testing the waters and not have a long-term commitment to NCC investing</li>
    <li class="q"><svg viewBox="0 0 20 20"><polygon class="bullet" points="1,2 6,2 10,10 14,2 19,2 10,19"/></svg><strong>Question #3: What percentage of the firm’s voting investment committee are full-time Non-Control Capital investors?</strong><br><span class="best">Best Answer</span>: Super-majority - Indicates commitment, experience, and focus on NCC and overcomes dependency on buyout heritage, if any</li>
    <li class="q"><svg viewBox="0 0 20 20"><polygon class="bullet" points="1,2 6,2 10,10 14,2 19,2 10,19"/></svg><strong>Question #4: What is the number of Non-Control Capital investments made with the <span class="u">current firm and team</span>?</strong><br><span class="best">Best Answer</span>: 20+ - Indicates long-term experience and comfort with current team, investment committee, and NCC investment assessment</li>
    <li class="q"><svg viewBox="0 0 20 20"><polygon class="bullet" points="1,2 6,2 10,10 14,2 19,2 10,19"/></svg><strong>Question #5: What percentage of portfolio investments made are “sponsorless” (those without a change-of-control investor)?</strong><span class="best">Best Answer</span>: 80%+ of all investments closed in the last 5 years (assumes current transaction is also sponsorless) Indicates ability to add-value as a sole minority investor and not simply as a back-up to another sponsor</li>
    <li class="q q--wide"><svg viewBox="0 0 20 20"><polygon class="bullet" points="1,2 6,2 10,10 14,2 19,2 10,19"/></svg><strong>Question #6: Can the investor show quantifiable proof of their ability to assist portfolio companies with growth and improvement (assumes more than 20 exited Non-Control investments)?:</strong><br><span class="best">Best Answer</span>: Yes (company owners should evaluate investors on actual historical revenue, EBITDA, and employee growth impact and the results should exceed what the current management has achieved on their own over the past 3 years) - Indicates true value-added ability to help owners grow their businesses. Those without proof of their impact, or who are unwilling to disclose it, should be excluded</li>
  </ul>
  <div class="brand"><span class="brand-square"></span><span class="brand-name">Ridgeholm</span></div>
  <div class="foot-bar"></div>
  <div class="foot-square"></div>
</section>

<!-- Option D: ring bullets -->
<section class="slide slide--br">
  <div class="side-panel"></div>
  <div class="title-bar"></div>
  <h1 class="title">THE CRITICAL QUESTIONS TO ASK OF ANY PROSPECTIVE NON-CONTROL INVESTOR</h1>
  <p class="subtitle">Non-Control Capital is a specialty, so only those firms with deep experience investing it as a team should be considered</p>
  <p class="tag">Non-Control Capital Questionnaire</p>
  <ul class="questions">
    <li class="q"><svg viewBox="0 0 20 20"><ellipse class="bullet-ring" cx="10" cy="10" rx="6" ry="7.5"/></svg><strong>Question #1: How many years has the firm been investing Non-Control Capital?</strong><br><span class="best">Best Answer</span>: 5+ years investing as a team within the current firm<br>Indicates comfort and experience evaluating and making NCC investments with each other and increases likelihood of close</li>
    <li class="q"><svg viewBox="0 0 20 20"><ellipse class="bullet-ring" cx="10" cy="10" rx="6" ry="7.5"/></svg><strong>Question #2: How may fully-invested Non-Control Capital funds in the firm’s history?</strong><br><span class="best">Best Answer</span>: 2+ fully-invested funds - Indicates experience and ability to close deals with the current regime—those firms without it may only be testing the waters and not have a long-term commitment to NCC investing</li>
    <li class="q"><svg viewBox="0 0 20 20"><ellipse class="bullet-ring" cx="10" cy="10" rx="6" ry="7.5"/></svg><strong>Question #3: What percentage of the firm’s voting investment committee are full-time Non-Control Capital investors?</strong><br><span class="best">Best Answer</span>: Super-majority - Indicates commitment, experience, and focus on NCC and overcomes dependency on buyout heritage, if any</li>
    <li class="q"><svg viewBox="0 0 20 20"><ellipse class="bullet-ring" cx="10" cy="10" rx="6" ry="7.5"/></svg><strong>Question #4: What is the number of Non-Control Capital investments made with the <span class="u">current firm and team</span>?</strong><br><span class="best">Best Answer</span>: 20+ - Indicates long-term experience and comfort with current team, investment committee, and NCC investment assessment</li>
    <li class="q"><svg viewBox="0 0 20 20"><ellipse class="bullet-ring" cx="10" cy="10" rx="6" ry="7.5"/></svg><strong>Question #5: What percentage of portfolio investments made are “sponsorless” (those without a change-of-control investor)?</strong><span class="best">Best Answer</span>: 80%+ of all investments closed in the last 5 years (assumes current transaction is also sponsorless) Indicates ability to add-value as a sole minority investor and not simply as a back-up to another sponsor</li>
    <li class="q q--wide"><svg viewBox="0 0 20 20"><ellipse class="bullet-ring" cx="10" cy="10" rx="6" ry="7.5"/></svg><strong>Question #6: Can the investor show quantifiable proof of their ability to assist portfolio companies with growth and improvement (assumes more than 20 exited Non-Control investments)?:</strong><br><span class="best">Best Answer</span>: Yes (company owners should evaluate investors on actual historical revenue, EBITDA, and employee growth impact and the results should exceed what the current management has achieved on their own over the past 3 years) - Indicates true value-added ability to help owners grow their businesses. Those without proof of their impact, or who are unwilling to disclose it, should be excluded</li>
  </ul>
  <div class="brand"><span class="brand-square"></span><span class="brand-name">Ridgeholm</span></div>
  <div class="foot-bar"></div>
  <div class="foot-square"></div>
</section>

</body>
</html>
```